Financial Advisor Resource Firm needs business card design

Need business card design for company in Omaha NE called Tallowbrook Partners. We provide resources to financial advisors....workshop programs, retirement analysis, and insurance planning. I would like to see designs that use grays, greens, black, and white colors. The final design should communicate 'collaboration' and be simple yet attractive to financial planning clients. I will attached our logo and another picture of a puzzle piece coming together. I would like the incorporate the puzzle picture somehow, maybe on the back somehow, with color or just the gray scale....OR, the picture be the front of the card with 'Tallowbrook' definition on it (see upload) and then company logo, employee name, title, address on the back (see ppt uploaded). The following disclosure needs to be included somewhere- Advisory services offered through Marlowe Ridge Advisors, LLC.
Updates

I uploaded a svg and ai file of the logo

Target Market(s)

Financial planning clients and financial advisors....so pretty diverse age range of about 40-70.

Industry/Entity Type

Financial Planning

Contact Information for Business Card

Dennis K. Holloway, MBA
Founder/President
5727 E. Larkspur Avenue
Suite 418
Omaha, NE 68297
Phone- (402) 555-0147
Cell- (402) 555-0183
Fax- (402) 555-0129
email- dennis@tallowbrookgroup.example
web address- www.tallowbrookgroup.example

Colors
1b1b1b
474747
d3d3d3
ffffff
9bcb3c
abd036

Requirements
Must have
• Must include logo provided, must be 2 sided, and must have disclosure...all of these items listed in project description

```html
<!DOCTYPE html>
<html lang="en">
<head>
<meta charset="utf-8">
<title>Tallowbrook Partners – Business Card</title>
<link href="https://fonts.googleapis.com/css2?family=Cinzel:wght@400&family=Source+Sans+3:wght@400;600;700&family=Noto+Serif:wght@400&display=swap" rel="stylesheet">
<style>
  :root {
    --ink: #1b1b1b;
    --charcoal: #474747;
    --mist: #d3d3d3;
    --paper: #f4f4f2;
    --white: #ffffff;
    --leaf: #8bbf3f;
    --leaf-bright: #9bcb3c;
    --backdrop: #e2e2e2;
  }
  * { box-sizing: border-box; margin: 0; padding: 0; }
  html, body { width: 1200px; height: 900px; overflow: hidden; }
  body {
    background: var(--backdrop);
    font-family: "Source Sans 3", Arial, sans-serif;
    color: var(--ink);
    position: relative;
  }
  .card {
    position: absolute;
    left: 250px;
    width: 700px;
    height: 400px;
    overflow: hidden;
    box-shadow: 0 2px 8px rgba(0,0,0,.12);
  }
  .card--front { top: 40px; background: var(--leaf); }
  .card--back { top: 460px; background: var(--paper); }

  /* front */
  .front-photo {
    position: absolute; left: 0; top: 0; width: 700px; height: 180px;
    background: linear-gradient(100deg, #5a5a5a 0%, #9a9a9a 35%, #c8c8c8 55%, #7d7d7d 80%, #4a4a4a 100%);
  }
  .front-band {
    position: absolute; left: 0; top: 180px; width: 700px; height: 112px;
    background: var(--leaf);
  }
  .front-word {
    position: absolute; left: 0; right: 0; top: 196px;
    text-align: center;
    font-family: "Cinzel", "Times New Roman", serif;
    font-size: 50px;
    letter-spacing: 22px;
    color: var(--ink);
    line-height: 1;
  }
  .front-word .dot { letter-spacing: 22px; }
  .front-phonetic {
    position: absolute; left: 0; right: 0; top: 254px;
    text-align: center;
    font-family: "Noto Serif", Georgia, serif;
    font-size: 24px;
    color: var(--ink);
  }
  .front-definition {
    position: absolute; left: 0; top: 292px; width: 700px; height: 46px;
    background: var(--ink);
    color: var(--white);
    font-size: 20px;
    line-height: 46px;
    padding-left: 40px;
  }

  /* back */
  .back-shape { position: absolute; left: 0; top: 0; }
  .contact {
    position: absolute; left: 34px; top: 30px; width: 310px;
  }
  .contact-name { font-size: 27px; font-weight: 700; line-height: 1.1; }
  .contact-title {
    font-size: 17px; letter-spacing: 3px; color: var(--ink); margin-top: 2px;
  }
  .contact-list { list-style: none; margin-top: 14px; }
  .contact-list li {
    display: flex; align-items: flex-start; gap: 12px;
    font-size: 16.5px; line-height: 1.25; margin-bottom: 7px;
  }
  .contact-list svg { flex: none; width: 18px; height: 18px; margin-top: 1px; }
  .contact-rule {
    border: 0; border-top: 1px solid var(--ink); opacity: .55;
    margin: 12px 0 14px;
  }
  .contact-web { font-size: 17px; font-weight: 700; margin-top: 8px; }

  .brand {
    position: absolute; left: 400px; top: 120px; width: 270px;
    text-align: center;
  }
  .brand-name {
    display: flex; align-items: center; justify-content: center; gap: 10px;
    font-size: 26px; font-weight: 600; letter-spacing: 1.5px;
    color: var(--ink); line-height: 1;
  }
  .brand-dot {
    width: 16px; height: 16px; border-radius: 50%; background: var(--leaf-bright);
  }
  .brand-rule { border: 0; border-top: 1.5px solid var(--charcoal); margin: 18px 0 14px; }
  .brand-disclosure { font-size: 17px; line-height: 1.2; color: var(--ink); }
</style>
</head>
<body>

<section class="card card--front" aria-label="Card front">
  <div class="front-photo" role="img" aria-label="Grayscale photo of several hands joining puzzle pieces together"></div>
  <div class="front-band"></div>
  <p class="front-word">TAL<span class="dot">·</span>LOW<span class="dot">·</span>BROOK</p>
  <p class="front-phonetic">ˈta-lō-ˌbru̇k</p>
  <p class="front-definition">: to come together and unite in common interest and focus</p>
</section>

<section class="card card--back" aria-label="Card back">
  <svg class="back-shape" width="700" height="400" viewBox="0 0 700 400" aria-hidden="true">
    <rect x="0" y="0" width="358" height="400" fill="var(--charcoal)"/>
    <polygon points="0,0 342,0 342,128 372,150 342,172 342,400 0,400" fill="var(--leaf)"/>
  </svg>

  <div class="contact">
    <h1 class="contact-name">Dennis K. Holloway, MBA</h1>
    <p class="contact-title">FOUNDER/PRESIDENT</p>
    <ul class="contact-list">
      <li>
        <svg viewBox="0 0 18 18"><rect x="4.5" y="1" width="9" height="16" rx="1.5" fill="none" stroke="var(--ink)" stroke-width="1.6"/><line x1="7.5" y1="14.5" x2="10.5" y2="14.5" stroke="var(--ink)" stroke-width="1.4"/></svg>
        (402) 555-0183
      </li>
      <li>
        <svg viewBox="0 0 18 18"><rect x="1" y="4" width="16" height="11" fill="var(--ink)"/><polyline points="1.5,4.5 9,10.5 16.5,4.5" fill="none" stroke="var(--leaf)" stroke-width="1.4"/></svg>
        dennis@tallowbrookgroup.example
      </li>
    </ul>
    <hr class="contact-rule">
    <ul class="contact-list">
      <li>
        <svg viewBox="0 0 18 18"><path d="M4 1.5l3 3.5-1.8 2.2c1 2 2.6 3.6 4.6 4.6L12 10l3.5 3-1.5 3c-6.5-.3-12-5.8-12.5-12.5z" fill="var(--ink)"/></svg>
        (402) 555-0147
      </li>
      <li>
        <svg viewBox="0 0 18 18"><rect x="1" y="6" width="16" height="11" rx="1" fill="var(--ink)"/><rect x="4" y="1" width="10" height="6" fill="none" stroke="var(--ink)" stroke-width="1.5"/><rect x="4" y="9" width="10" height="2" fill="var(--leaf)"/><rect x="4" y="13" width="2" height="2" fill="var(--leaf)"/><rect x="8" y="13" width="2" height="2" fill="var(--leaf)"/><rect x="12" y="13" width="2" height="2" fill="var(--leaf)"/></svg>
        (402) 555-0129
      </li>
      <li>
        <svg viewBox="0 0 18 18"><path d="M9 1a5.5 5.5 0 0 0-5.5 5.5C3.5 11 9 17 9 17s5.5-6 5.5-10.5A5.5 5.5 0 0 0 9 1z" fill="var(--ink)"/><circle cx="9" cy="6.5" r="2" fill="var(--leaf)"/></svg>
        <span>5727 E. Larkspur Avenue • Suite 418<br>Omaha, NE 68297</span>
      </li>
    </ul>
    <p class="contact-web">www.tallowbrookgroup.example</p>
  </div>

  <div class="brand">
    <p class="brand-name"><span class="brand-dot"></span>TALLOWBROOK PARTNERS</p>
    <hr class="brand-rule">
    <p class="brand-disclosure">Advisory services offered<br>through Marlowe Ridge Advisors, LLC.</p>
  </div>
</section>

</body>
</html>
```